Business Card Design Project

We need a business card for a chiropractic and rehabilitation center. We already have a logo and need the card to follow the color and feel of the logo.

Target Market(s)

adults 30-55 that have some ache or pain that is interfering with their life, so much as they are ready to do something about it.

Industry/Entity Type

Business

```html
<!DOCTYPE html>
<html lang="en">
<head>
<meta charset="utf-8">
<title>Corepath Wellness – Business Card</title>
<link rel="stylesheet" href="https://fonts.googleapis.com/css2?family=Arimo:wght@400&family=Federo&display=swap">
<style>
  :root {
    --page: #ffffff;
    --card: #f5f5f3;
    --orange: #f6962c;
    --ring: #4a4a4c;
    --red: #c62a3b;
    --grey: #555557;
    --ink: #111111;
    --on-orange: #ffffff;
  }
  * { margin: 0; padding: 0; box-sizing: border-box; }
  html, body {
    width: 1080px; height: 1200px; overflow: hidden;
    background: var(--page);
    font-family: "Arimo", Arial, sans-serif;
  }
  .card {
    position: absolute; left: 0; top: 0;
    width: 1080px; height: 630px;
    background: var(--card);
    overflow: hidden;
  }
  .card__shapes { position: absolute; inset: 0; }
  .holder { position: absolute; }
  .holder__name {
    left: 48px; top: 38px;
    font-family: "Federo", sans-serif;
    font-size: 54px; color: var(--red); line-height: 1; white-space: nowrap;
  }
  .holder__title {
    left: 232px; top: 100px; width: 233px; text-align: right;
    font-size: 27px; color: var(--grey); white-space: nowrap;
  }
  .brand {
    position: absolute; left: 60px; top: 290px;
    display: flex; align-items: center; gap: 20px;
  }
  .brand__mark {
    width: 58px; height: 58px; border-radius: 50%;
    border: 6px solid var(--orange); flex: none;
  }
  .brand__name {
    font-size: 50px; color: var(--grey); letter-spacing: 1px; line-height: 1;
    white-space: nowrap;
  }
  .contact {
    position: absolute; left: 744px; top: 152px;
    color: var(--on-orange);
  }
  .contact__label { font-size: 29px; line-height: 34px; }
  .contact__value { font-size: 29px; line-height: 36px; margin-bottom: 16px; }
  .contact__value--small { font-size: 24px; margin-bottom: 14px; }
  .address {
    position: absolute; left: 116px; top: 548px;
    font-size: 29px; color: var(--ink); white-space: nowrap;
  }
</style>
</head>
<body>
  <section class="card">
    <svg class="card__shapes" width="1080" height="630" viewBox="0 0 1080 630" aria-hidden="true">
      <circle cx="999" cy="327" r="334" fill="var(--orange)" stroke="var(--ring)" stroke-width="7"/>
      <circle cx="39" cy="587" r="73" fill="var(--orange)" stroke="var(--ring)" stroke-width="7"/>
    </svg>

    <div class="holder holder__name">Rosalind Hartwell</div>
    <div class="holder holder__title">Managing Director</div>

    <div class="brand">
      <span class="brand__mark"></span>
      <span class="brand__name">Corepath Wellness</span>
    </div>

    <div class="contact">
      <p class="contact__label">Phone:</p>
      <p class="contact__value">555.0142.316</p>
      <p class="contact__label">Fax:</p>
      <p class="contact__value">555.0142.317</p>
      <p class="contact__label">Email:</p>
      <p class="contact__value contact__value--small">info@corepathclinic.com</p>
      <p class="contact__label">Website:</p>
      <p class="contact__value contact__value--small">www.corepathclinic.com</p>
    </div>

    <p class="address">240 Mill Road, Suite 3,&nbsp; Lakeview, NJ 07999</p>
  </section>
</body>
</html>
```